Medical Practice Business Card

we need a business card for our new medical ophthalmology practice based in Needham Massachusetts. we are looking for a simple , modern and elegant design.
the card needs to contain the following
1- the logo of our practice (please see attached file)
2- the name of the practice : "Silver Birch Retina Care"
3- Doctor's Name: Tobias Rendell MD PhD
4- Specialty: Board-Certified Vitreoretinal Surgeon
5- practice address: 87 Larkspur Ave, Suite 210, Needham MA 02481
7- Office number: 617- 482 - 7730
8- fax number: 617- 391 - 2268
9- email: info@sbretinahub.example
10- website: www.sbretinahub.example

```html
<!DOCTYPE html>
<html lang="en">
<head>
<meta charset="utf-8">
<title>Silver Birch Retina Care – Business Card</title>
<link rel="stylesheet" href="https://fonts.googleapis.com/css2?family=Poppins:wght@300;400;600&display=swap">
<style>
  :root {
    --backdrop: #dfe7ec;
    --card-light: #f6f7f8;
    --card-shade: #e6e9ec;
    --ink-navy: #1c2b4d;
    --ink-blue: #3f5b86;
    --ring-blue: #2f6fa3;
  }
  * { margin: 0; padding: 0; box-sizing: border-box; }
  html, body {
    width: 1200px;
    height: 1200px;
    overflow: hidden;
    background: var(--backdrop);
    font-family: "Poppins", sans-serif;
  }
  .canvas {
    position: relative;
    width: 1200px;
    height: 1200px;
  }
  .business-card {
    position: absolute;
    left: 100px;
    top: 314px;
    width: 1000px;
    height: 572px;
    border-radius: 34px;
    background: linear-gradient(150deg, var(--card-light) 0%, var(--card-shade) 100%);
    box-shadow: 0 18px 40px rgba(28, 43, 77, 0.14);
    color: var(--ink-navy);
  }
  .practice-mark {
    position: absolute;
    top: 54px;
    right: 62px;
    display: flex;
    align-items: center;
    gap: 16px;
  }
  .practice-mark svg { display: block; }
  .practice-name {
    font-weight: 400;
    font-size: 27px;
    line-height: 1.12;
    color: var(--ink-navy);
    letter-spacing: 0.04em;
  }
  .doctor {
    position: absolute;
    left: 66px;
    top: 196px;
  }
  .doctor-name {
    font-weight: 600;
    font-size: 31px;
    letter-spacing: 0.01em;
    color: var(--ink-navy);
  }
  .doctor-title {
    margin-top: 2px;
    font-weight: 300;
    font-size: 20px;
    color: var(--ink-blue);
  }
  .office-details {
    position: absolute;
    left: 66px;
    bottom: 60px;
    font-weight: 400;
    font-size: 19px;
    line-height: 1.65;
    color: var(--ink-navy);
  }
  .web-details {
    position: absolute;
    right: 62px;
    top: 262px;
    text-align: right;
    font-weight: 400;
    font-size: 19px;
    line-height: 1.65;
    color: var(--ink-navy);
  }
</style>
</head>
<body>
<main class="canvas">
  <section class="business-card">
    <div class="practice-mark">
      <svg width="58" height="58" viewBox="0 0 58 58" aria-hidden="true">
        <circle cx="29" cy="29" r="26" fill="none" stroke="var(--ring-blue)" stroke-width="3"/>
      </svg>
      <p class="practice-name">Silver Birch<br>Retina Care</p>
    </div>

    <div class="doctor">
      <h1 class="doctor-name">TOBIAS RENDELL MD PHD</h1>
      <p class="doctor-title">Board-Certified Vitreoretinal Surgeon</p>
    </div>

    <div class="web-details">
      <p class="email">info@sbretinahub.example</p>
      <p class="website">www.sbretinahub.example</p>
    </div>

    <div class="office-details">
      <p class="office-phone">Office number: 617- 482 - 7730</p>
      <p class="office-fax">fax number: 617- 391 - 2268</p>
      <p class="office-address">87 Larkspur Ave, Suite 210, Needham MA 02481</p>
    </div>
  </section>
</main>
</body>
</html>
```